3.5" x 11" Door Hanger Design - Residential Roofing Company

We are looking for a double-sided door hanger that we can hang on the doors of prospects. This door hanger would have some brief information about our company, a phone number, website, and then the services that we offer. I don't know that it will have enough room for a lot of pictures, but feel free to use those from the marketing brochure if you think it'll work and I can get you the original as needed.
I have uploaded our certifications, logo, and then our current marketing brochure. The design should be cohesive with our marketing brochure, but doesn't have to match it perfectly.
Lastly, attached is the template that we are planning to print off of. This has a tear off portion at the bottom for a business card for a sales rep. The size of the overall door hanger will be 3.5" x 11", with the bottom 2.5" being the tear off business card with the salesman's information. I'll get you the sales reps information during the final design phase, but we will need name, title, phone number, email, business address, business website, list of services, and then the words "AZ ROC 562071" all on that small portion as well so if they tear it off they still have all the info.

```html
<!DOCTYPE html>
<html lang="en">
<head>
<meta charset="utf-8">
<title>Granite Ridge Roofing – Door Hanger</title>
<link rel="stylesheet" href="https://fonts.googleapis.com/css2?family=Roboto+Slab:wght@300;400;700;900&display=swap">
<style>
  :root {
    --paper: #ececec;
    --orange: #dd5324;
    --charcoal: #2d2d2d;
    --white: #ffffff;
    --photo-dark: #3a2a24;
    --photo-mid: #8a3a1f;
    --photo-grey: #5a5250;
    --photo-warm: #c4532a;
    --slab: "Roboto Slab", "Rockwell", "Zilla Slab", "Courier New", serif;
  }
  html, body {
    margin: 0;
    padding: 0;
    width: 1200px;
    height: 3681px;
    overflow: hidden;
    background: var(--paper);
  }
  .door-hanger {
    position: relative;
    width: 1200px;
    height: 3681px;
    background: var(--paper);
    overflow: hidden;
    font-family: var(--slab);
  }
  .artwork {
    position: absolute;
    inset: 0;
    width: 1200px;
    height: 3681px;
  }
  .headline {
    font-family: var(--slab);
    font-weight: 900;
    fill: var(--white);
  }
  .service-title {
    font-family: var(--slab);
    font-weight: 900;
    font-size: 57px;
    fill: var(--white);
  }
  .service-item {
    font-family: var(--slab);
    font-weight: 300;
    font-size: 46px;
    fill: var(--white);
  }
  .brand-name {
    font-family: var(--slab);
    font-weight: 900;
    font-size: 54px;
    fill: var(--charcoal);
  }
  .contact-text {
    font-family: var(--slab);
    font-weight: 400;
    font-size: 58px;
    fill: var(--charcoal);
  }
  .visit-word {
    font-family: var(--slab);
    font-weight: 900;
    font-size: 318px;
  }
  .visit-orange { fill: var(--orange); }
  .visit-dark { fill: var(--charcoal); }
</style>
</head>
<body>
<main class="door-hanger">
  <svg class="artwork" viewBox="0 0 1200 3681" xmlns="http://www.w3.org/2000/svg">
    <defs>
      <linearGradient id="roofPhotoTone" x1="0" y1="0" x2="0.7" y2="1">
        <stop offset="0" stop-color="var(--photo-mid)"/>
        <stop offset="0.35" stop-color="var(--photo-dark)"/>
        <stop offset="0.75" stop-color="var(--photo-mid)"/>
        <stop offset="1" stop-color="var(--photo-warm)"/>
      </linearGradient>
      <linearGradient id="roofRightTone" x1="0" y1="0" x2="0" y2="1">
        <stop offset="0" stop-color="var(--photo-grey)"/>
        <stop offset="1" stop-color="var(--photo-mid)"/>
      </linearGradient>
    </defs>

    <!-- top accent arrow -->
    <polygon class="accent-arrow" points="917,574 1057,494 1057,654" fill="var(--charcoal)"/>

    <!-- top-left orange wedge -->
    <polygon class="corner-wedge" points="0,760 180,857 0,868" fill="var(--orange)"/>

    <!-- roof photo area -->
    <g class="roof-photo" role="img" aria-label="Photo of a house with a red clay tile roof, a dark gable and brick walls">
      <polygon points="0,868 657,807 693,804 800,1157 1200,1143 1200,1550 329,2057 0,2236" fill="url(#roofPhotoTone)"/>
      <polygon points="800,1157 1200,1143 1200,1550 930,1700" fill="url(#roofRightTone)" opacity="0.8"/>
      <polygon points="0,1300 657,807 693,804 800,1157 329,2057 0,2236" fill="var(--orange)" opacity="0.22"/>
    </g>

    <!-- headline -->
    <text class="headline" x="410" y="1348" font-size="112" text-anchor="middle" textLength="593" lengthAdjust="spacingAndGlyphs">QUALITY</text>
    <text class="headline" x="410" y="1468" font-size="112" text-anchor="middle" textLength="600" lengthAdjust="spacingAndGlyphs">ROOFING</text>
    <text class="headline" x="413" y="1590" font-size="112" text-anchor="middle" textLength="585" lengthAdjust="spacingAndGlyphs">YOU CAN</text>
    <text class="headline" x="410" y="1740" font-size="150" text-anchor="middle" textLength="590" lengthAdjust="spacingAndGlyphs">TRUST!</text>

    <!-- services panel -->
    <polygon class="services-panel" points="1200,1550 1200,2543 329,2057" fill="var(--orange)"/>
    <text class="service-title" x="564" y="2024" text-anchor="middle">Our</text>
    <text class="service-title" x="564" y="2087" text-anchor="middle">Service</text>

    <g class="service-list">
      <circle cx="739" cy="1878" r="12" fill="var(--charcoal)"/>
      <text class="service-item" x="769" y="1893">Tile Roofing</text>
      <circle cx="739" cy="1990" r="12" fill="var(--charcoal)"/>
      <text class="service-item" x="769" y="2006">Metal Roofing</text>
      <circle cx="739" cy="2099" r="12" fill="var(--charcoal)"/>
      <text class="service-item" x="769" y="2114">Shingle Roofing</text>
      <circle cx="739" cy="2211" r="12" fill="var(--charcoal)"/>
      <text class="service-item" x="769" y="2205">Low Slope</text>
      <text class="service-item" x="769" y="2249">&amp; Coatings</text>
    </g>

    <!-- brand name -->
    <rect class="brand-mark" x="84" y="2270" width="32" height="32" fill="var(--orange)"/>
    <text class="brand-name" x="130" y="2304" textLength="460" lengthAdjust="spacingAndGlyphs">Granite Ridge Roofing</text>

    <!-- divider -->
    <line class="divider" x1="77" y1="2443" x2="776" y2="2443" stroke="var(--charcoal)" stroke-width="6" stroke-linecap="round"/>

    <!-- contact: website -->
    <g class="contact-icon" transform="translate(126,2579)">
      <polygon points="0,-50 43,-25 43,25 0,50 -43,25 -43,-25" fill="var(--charcoal)"/>
      <g fill="none" stroke="var(--white)" stroke-width="3.5">
        <circle r="22"/>
        <ellipse rx="10" ry="22"/>
        <line x1="-22" y1="0" x2="22" y2="0"/>
        <line x1="-19" y1="-11" x2="19" y2="-11"/>
        <line x1="-19" y1="11" x2="19" y2="11"/>
      </g>
    </g>
    <text class="contact-text" x="207" y="2598">graniteridge-roofing.com</text>

    <!-- contact: address -->
    <g class="contact-icon" transform="translate(126,2724)">
      <polygon points="0,-50 43,-25 43,25 0,50 -43,25 -43,-25" fill="var(--orange)"/>
      <path d="M0,26 C-8,14 -18,3 -18,-8 A18,18 0 0 1 18,-8 C18,3 8,14 0,26 Z" fill="var(--white)"/>
      <circle cy="-8" r="7" fill="var(--orange)"/>
    </g>
    <text class="contact-text" x="207" y="2716">418 N Pine Ave,</text>
    <text class="contact-text" x="207" y="2774">Cedar Falls AZ 86305</text>

    <!-- contact: phone -->
    <g class="contact-icon" transform="translate(126,2871)">
      <polygon points="0,-50 43,-25 43,25 0,50 -43,25 -43,-25" fill="var(--charcoal)"/>
      <path d="M-16,-20 l9,-3 7,13 -6,5 c3,7 8,12 15,15 l5,-6 13,7 -3,9 c-2,4 -6,5 -10,4 C-3,18 -17,4 -21,-10 c-1,-4 1,-9 5,-10 Z" fill="var(--white)"/>
      <path d="M6,-18 a14,14 0 0 1 13,13 M6,-27 a23,23 0 0 1 22,22" fill="none" stroke="var(--white)" stroke-width="3.5" stroke-linecap="round"/>
    </g>
    <text class="contact-text" x="207" y="2891">(928) 555-0147</text>

    <!-- bottom accent arrows -->
    <polygon class="accent-arrow" points="947,2779 1086,2699 1086,2857" fill="var(--charcoal)"/>
    <polygon class="accent-arrow" points="947,2846 1014,2884 947,2923" fill="var(--orange)"/>

    <!-- visit call-out -->
    <text class="visit-word" x="597" y="3447" text-anchor="middle" textLength="929" lengthAdjust="spacingAndGlyphs"><tspan class="visit-orange">V</tspan><tspan class="visit-dark">I</tspan><tspan class="visit-orange">S</tspan><tspan class="visit-dark">I</tspan><tspan class="visit-orange">T</tspan></text>
  </svg>
</main>
</body>
</html>
```